body balm label design

body balm tube design, current label design for other similar products
Need to have a design which can interchange between 3 different solutions
Amber Tide (Lavender + Vanilla)
Copper Harbor (Eucalyptus + Mint)
Velvet Arc (Bergamot + Cedarwood)
Tube size:
2.5h x 3.25 w
Target Market(s)
natural, solution focused
Requirements
Must have
- relatable to existing brand designs, focus on features and benefits

```html
<!DOCTYPE html>
<html lang="en">
<head>
<meta charset="utf-8">
<title>Willowmere Natural Body Balm Labels</title>
<link rel="stylesheet" href="https://fonts.googleapis.com/css2?family=Cormorant+Garamond:wght@500&family=Allura&family=Montserrat:wght@300;400;600&display=swap">
<style>
  :root {
    --page: #eef0f4;
    --paper: #ffffff;
    --slate: #8b9ca8;
    --sage: #b9cbab;
    --leaf: #76a45e;
    --fine-text: #9a9a9a;
  }
  * { margin: 0; padding: 0; box-sizing: border-box; }
  html, body { width: 1059px; height: 1200px; overflow: hidden; background: var(--page); }
  .sheet {
    width: 1059px; height: 1200px;
    display: flex; flex-direction: column; align-items: center;
    justify-content: space-evenly;
  }
  .label {
    position: relative; width: 481px; height: 370px;
    background: var(--paper); overflow: hidden;
    font-family: "Montserrat", sans-serif;
  }
  .label--amber  { --accent: var(--slate); --fine: var(--fine-text); }
  .label--velvet { --accent: var(--sage);  --fine: #b9c3b2; }
  .label--copper { --accent: var(--leaf);  --fine: var(--fine-text); }

  .botanical {
    position: absolute; left: 20px; top: 10px; width: 330px; height: 350px;
    background: radial-gradient(ellipse at 50% 50%, color-mix(in srgb, var(--accent) 16%, transparent) 0%, transparent 70%);
  }
  .title {
    position: absolute; right: 142px; top: 50px;
    font-family: "Cormorant Garamond", serif; font-weight: 500;
    font-size: 66px; line-height: 66px; letter-spacing: 8px;
    color: var(--accent);
  }
  .title-rule {
    position: absolute; left: 0; top: 124px; width: 264px; height: 2px;
    background: var(--accent);
  }
  .subtitle {
    position: absolute; right: 148px; top: 110px;
    font-family: "Allura", cursive; font-size: 30px; line-height: 30px;
    color: var(--accent);
  }
  .band {
    position: absolute; left: 0; top: 143px; width: 346px; height: 75px;
    background: var(--accent); border-radius: 0 38px 38px 0;
  }
  .band-text {
    position: absolute; left: 0; top: 8px; width: 320px;
    text-align: center; color: #fff; font-weight: 300;
    font-size: 25px; line-height: 30px; letter-spacing: 1px;
  }
  .maker-mark {
    position: absolute; right: 10px; top: 10px; width: 55px; height: 55px;
    border: 1px solid rgba(255,255,255,.85); border-radius: 50%;
    display: flex; align-items: center; justify-content: center;
    color: #fff; font-size: 7.5px; font-weight: 400; letter-spacing: .5px;
  }
  .scent {
    position: absolute; left: 0; top: 228px; width: 346px; text-align: center;
    font-family: "Allura", cursive; font-size: 38px; line-height: 44px;
    color: var(--accent);
  }
  .net-weight {
    position: absolute; left: 82px; top: 311px;
    font-size: 12px; font-weight: 300; color: var(--accent);
  }
  .seal {
    position: absolute; left: 280px; top: 295px; width: 50px; height: 50px;
    border-radius: 50%; border: 1px solid var(--accent); opacity: .7;
  }
  .details {
    position: absolute; left: 383px; top: 66px; width: 92px;
    font-size: 8px; line-height: 9.8px; letter-spacing: .4px; color: var(--fine);
  }
  .details h4 { font-size: 8px; font-weight: 600; color: var(--accent); margin-bottom: 3px; letter-spacing: .6px; }
  .details p { margin-bottom: 8px; }
  .follow {
    position: absolute; left: 362px; top: 302px; width: 112px; text-align: center;
    font-size: 7.5px; line-height: 11px; letter-spacing: .6px; color: var(--fine);
  }
  .follow .site { color: var(--accent); font-weight: 600; }
</style>
</head>
<body>
<main class="sheet">

  <section class="label label--amber">
    <div class="botanical" role="img" aria-label="Fine line drawing of lavender and vanilla flowers"></div>
    <div class="title">AMBER</div>
    <div class="title-rule"></div>
    <div class="subtitle">tide</div>
    <div class="band">
      <div class="band-text">NATURAL<br>BODY BALM</div>
      <div class="maker-mark">Willowmere</div>
    </div>
    <div class="scent">Lavender + Vanilla</div>
    <div class="net-weight">NET WT 4 oz /120g</div>
    <div class="seal"></div>
    <div class="details">
      <h4>Ingredients:</h4>
      <p>Shea butter, cocoa butter, coconut oil, sweet almond oil, beeswax, lavender essential oil, vanilla extract or vanilla oleoresin, vitamin E oil</p>
      <h4>How to use:</h4>
      <p>Scoop a small amount, warm it between your palms, apply to dry skin areas, gently massage in, let it absorb, use as needed.</p>
    </div>
    <div class="follow">Made by Willowmere<br><span class="site">WWW.WILLOWMERE.CA</span></div>
  </section>

  <section class="label label--velvet">
    <div class="botanical" role="img" aria-label="Fine line drawing of bergamot fruit and blossoms"></div>
    <div class="title">VELVET</div>
    <div class="title-rule"></div>
    <div class="subtitle">arc</div>
    <div class="band">
      <div class="band-text">NATURAL<br>BODY BALM</div>
      <div class="maker-mark">Willowmere</div>
    </div>
    <div class="scent">Bergamot + Cedarwood</div>
    <div class="net-weight">NET WT 4 oz /120g</div>
    <div class="seal"></div>
    <div class="details">
      <h4>Ingredients:</h4>
      <p>Shea butter, cocoa butter, coconut oil, sweet almond oil, beeswax, lavender essential oil, vanilla extract or vanilla oleoresin, vitamin E oil</p>
      <h4>How to use:</h4>
      <p>Scoop a small amount, warm it between your palms, apply to dry skin areas, gently massage in, let it absorb, use as needed.</p>
    </div>
    <div class="follow">Made by Willowmere<br><span class="site">WWW.WILLOWMERE.CA</span></div>
  </section>

  <section class="label label--copper">
    <div class="botanical" role="img" aria-label="Fine line drawing of eucalyptus leaves and stems"></div>
    <div class="title">COPPER</div>
    <div class="title-rule"></div>
    <div class="subtitle">harbor</div>
    <div class="band">
      <div class="band-text">NATURAL<br>BODY BALM</div>
      <div class="maker-mark">Willowmere</div>
    </div>
    <div class="scent">Eucalyptus + Mint</div>
    <div class="net-weight">NET WT 4 oz /120g</div>
    <div class="seal"></div>
    <div class="details">
      <h4>Ingredients:</h4>
      <p>Shea butter, cocoa butter, coconut oil, sweet almond oil, beeswax, lavender essential oil, vanilla extract or vanilla oleoresin, vitamin E oil</p>
      <h4>How to use:</h4>
      <p>Scoop a small amount, warm it between your palms, apply to dry skin areas, gently massage in, let it absorb, use as needed.</p>
    </div>
    <div class="follow">Made by Willowmere<br><span class="site">WWW.WILLOWMERE.CA</span></div>
  </section>

</main>
</body>
</html>
```